Corvenne Jewelers Business Cards

A creative, cool edgy business card for our entire team that says we are a young, hip, luxury jewelry store specializing in diamonds and engagement rings but that we are also personal shoppers and trusted advisors. Our colors are Navy Blue & Platinum

I have included our past business card.

Font styles to use
Serif

Colors
0255a3

Requirements
Nice to have
• A card stock that you can write on with a pen

```html
<!DOCTYPE html>
<html lang="en">
<head>
<meta charset="utf-8">
<title>Corvenne Jewelers Business Cards</title>
<link rel="stylesheet" href="https://fonts.googleapis.com/css2?family=EB+Garamond:wght@400&family=Roboto+Slab:wght@700&family=Open+Sans:wght@400;600&display=swap">
<style>
  :root {
    --navy: #13215a;
    --navy-deep: #122058;
    --platinum: #e7e6e4;
    --ink: #1a1a1a;
    --rule: #a9a9a9;
    --backdrop: #7b7b7b;
    --white: #ffffff;
  }
  * { box-sizing: border-box; margin: 0; padding: 0; }
  html, body { width: 1200px; height: 1200px; overflow: hidden; }
  body { background: var(--backdrop); position: relative; font-family: "Open Sans", Arial, sans-serif; }

  .card {
    position: absolute;
    top: 310px;
    width: 364px;
    height: 594px;
    box-shadow: 2px 3px 6px rgba(0,0,0,0.35);
    text-align: center;
  }
  .card--front { left: 234px; background: var(--platinum); color: var(--ink); }
  .card--back { left: 632px; background: var(--navy-deep); color: var(--white); }

  .brand-dot {
    position: absolute;
    left: 50%;
    top: 90px;
    width: 90px;
    height: 90px;
    margin-left: -45px;
    border-radius: 50%;
    background: var(--navy);
  }
  .brand-name {
    position: absolute;
    left: 0; right: 0;
    font-family: "EB Garamond", Georgia, serif;
    font-variant: small-caps;
    font-weight: 400;
    font-size: 34px;
    letter-spacing: 0.5px;
    line-height: 1;
  }
  .card--front .brand-name { top: 242px; color: var(--navy); }
  .card--back .brand-name { top: 472px; color: var(--white); }

  .person { position: absolute; top: 344px; left: 0; right: 0; }
  .person__name {
    font-family: "Roboto Slab", Georgia, serif;
    font-weight: 700;
    font-size: 20px;
    color: var(--navy);
    letter-spacing: 0.3px;
    line-height: 1.15;
  }
  .person__title { font-size: 16px; line-height: 1.3; }

  .rule {
    position: absolute;
    left: 78px; right: 78px;
    height: 1px;
    background: var(--rule);
  }
  .rule--top { top: 396px; }
  .rule--bottom { top: 507px; }

  .contact {
    position: absolute;
    top: 405px;
    left: 0; right: 0;
    list-style: none;
    font-size: 16.5px;
    line-height: 21.5px;
  }
  .contact__label { color: var(--navy); font-weight: 600; }
  .contact__web { color: var(--navy); font-weight: 600; }

  .address {
    position: absolute;
    top: 514px;
    left: 0; right: 0;
    font-size: 16.5px;
    line-height: 21.5px;
    font-style: normal;
  }

  .card--back .site {
    position: absolute;
    top: 535px;
    left: 0; right: 0;
    font-size: 16.5px;
  }
</style>
</head>
<body>
  <section class="card card--front">
    <span class="brand-dot"></span>
    <h1 class="brand-name">Corvenne Jewelers</h1>

    <div class="person">
      <h2 class="person__name">JULIAN MARSH</h2>
      <p class="person__title">Managing Director</p>
    </div>
    <div class="rule rule--top"></div>

    <ul class="contact">
      <li><span class="contact__label">P:</span> 044-555 010 222</li>
      <li><span class="contact__label">M:</span> 044-555 010 222</li>
      <li><span class="contact__label">E:</span> hello@corvenne.com</li>
      <li class="contact__web">www.corvenne.com</li>
    </ul>
    <div class="rule rule--bottom"></div>

    <address class="address">12345, Address Goes Here<br>Country Name, 123456.</address>
  </section>

  <section class="card card--back">
    <h2 class="brand-name">Corvenne Jewelers</h2>
    <p class="site">www.corvenne.com</p>
  </section>
</body>
</html>
```